CALDERA
I need double sided standard sized Business Card [3.5" x 2"]
Open to designers choice
Professional
Tavo Berendsky
PO BOX 7312
ASHMORE, CA 90512
tavo@qrd4.com
WWW.QRD4.COM
IF YOU NEED ANOTHER FILE .PDF, .JPG, ETC. PLEASE LET ME KNOW

```html
<!DOCTYPE html>
<html lang="en">
<head>
<meta charset="utf-8">
<title>Caldera Stationery</title>
<link href="https://fonts.googleapis.com/css2?family=Arimo:wght@400;700&display=swap" rel="stylesheet">
<style>
  :root {
    --stage: #000000;
    --paper: #ffffff;
    --red: #b3121b;
    --red-deep: #7d0a10;
    --red-bright: #d2232a;
    --orange: #f39a2b;
    --orange-light: #fbb552;
    --gold: #f2b233;
    --ink-light: #ffffff;
  }
  * { box-sizing: border-box; margin: 0; padding: 0; }
  html, body { width: 1200px; height: 765px; overflow: hidden; background: var(--stage); }
  body { position: relative; font-family: "Arimo", Arial, sans-serif; }

  .piece { position: absolute; overflow: hidden; border-radius: 4px; }
  .wave { position: absolute; left: 0; bottom: 0; width: 100%; display: block; }

  .brand { position: absolute; display: flex; align-items: center; gap: 4px; }
  .brand-dot { width: 12px; height: 12px; border-radius: 50%; background: var(--gold); flex: none; }
  .brand-name { font-weight: 700; color: var(--red); letter-spacing: 0.5px; line-height: 1; }
  .brand.on-red .brand-name { color: var(--gold); }

  /* Letterhead */
  .letterhead { left: 36px; top: 53px; width: 516px; height: 662px; background: var(--paper); border-radius: 0; }
  .letterhead .brand { left: 24px; top: 44px; }
  .letterhead .brand-name { font-size: 18px; }
  .letterhead .footer-text { position: absolute; left: 24px; bottom: 14px; color: var(--ink-light); font-size: 8.5px; line-height: 1.45; }

  /* Business card front */
  .card-front { left: 562px; top: 53px; width: 211px; height: 120px; background: var(--paper); }
  .card-front .brand { left: 8px; top: 16px; }
  .card-front .brand-dot { width: 9px; height: 9px; }
  .card-front .brand-name { font-size: 11px; }
  .card-front .person { position: absolute; left: 74px; top: 44px; }
  .card-front .person-name { color: var(--red); font-size: 10px; font-weight: 700; }
  .card-front .person-title { color: var(--red); font-size: 7px; margin-top: 2px; padding-left: 24px; }
  .card-front .details { position: absolute; left: 9px; bottom: 9px; color: var(--ink-light); font-size: 5.5px; line-height: 1.4; }

  /* Card backs */
  .card-back { display: flex; align-items: center; justify-content: center; }
  .card-back .brand { position: static; }
  .card-back .brand-name { font-size: 16px; }
  .card-white { left: 871px; top: 108px; width: 211px; height: 120px; background: var(--paper); border-radius: 10px; }
  .card-red { left: 634px; top: 202px; width: 211px; height: 118px; background: radial-gradient(ellipse at center, var(--red-bright), var(--red-deep)); border-radius: 3px; }
  .card-orange { left: 902px; top: 252px; width: 209px; height: 120px; background: linear-gradient(180deg, var(--orange-light), var(--orange)); }

  /* Envelope */
  .envelope { left: 562px; top: 384px; width: 571px; height: 331px; background: var(--paper); border-radius: 10px 10px 0 0; }
  .envelope .flap { position: absolute; left: 0; top: 0; width: 100%; display: block; }
  .envelope .flap-brand { left: 50%; top: 22px; transform: translateX(-50%); }
  .envelope .flap-brand .brand-name { font-size: 14px; }
  .envelope .return-brand { left: 16px; top: 112px; }
  .envelope .return-brand .brand-name { font-size: 17px; }
  .envelope .footer-text { position: absolute; left: 14px; bottom: 18px; color: var(--ink-light); font-size: 8.5px; }
</style>
</head>
<body>

  <section class="piece letterhead">
    <div class="brand"><span class="brand-dot"></span><span class="brand-name">CALDERA</span></div>
    <svg class="wave" viewBox="0 0 516 120" height="120" preserveAspectRatio="none">
      <defs>
        <linearGradient id="lhRed" x1="0" y1="0" x2="0" y2="1">
          <stop offset="0" stop-color="var(--red-bright)"/><stop offset="1" stop-color="var(--red-deep)"/>
        </linearGradient>
      </defs>
      <path d="M0 24 Q260 52 516 20 L516 120 L0 120 Z" fill="var(--orange)"/>
      <path d="M0 30 Q260 58 516 28 L516 120 L0 120 Z" fill="url(#lhRed)"/>
    </svg>
    <div class="footer-text">
      <p>PO BOX 7312 ASHMORE, CA 90512</p>
      <p>Tel/Fax: 555 014 2290 | Phone: 555 017 3364 | Cell: 555 017 3364 | Fax: 5550142290</p>
      <p>Email: tavo@qrd4.com | WWW.QRD4.COM</p>
    </div>
  </section>

  <section class="piece card-front">
    <div class="brand"><span class="brand-dot"></span><span class="brand-name">CALDERA</span></div>
    <div class="person">
      <p class="person-name">Tavo Berendsky</p>
      <p class="person-title">CEO</p>
    </div>
    <svg class="wave" viewBox="0 0 211 50" height="50" preserveAspectRatio="none">
      <path d="M0 6 Q105 16 211 4 L211 50 L0 50 Z" fill="var(--orange)"/>
      <path d="M0 9 Q105 19 211 8 L211 50 L0 50 Z" fill="var(--red)"/>
    </svg>
    <div class="details">
      <p>PO BOX 7312 ASHMORE, CA 90512</p>
      <p>Tel: 555 014 2290 | Cell: 555 017 3364</p>
      <p>tavo@qrd4.com | WWW.QRD4.COM</p>
    </div>
  </section>

  <section class="piece card-back card-white">
    <div class="brand"><span class="brand-dot"></span><span class="brand-name">CALDERA</span></div>
  </section>

  <section class="piece card-back card-red">
    <div class="brand on-red"><span class="brand-dot"></span><span class="brand-name">CALDERA</span></div>
  </section>

  <section class="piece card-back card-orange">
    <div class="brand"><span class="brand-dot"></span><span class="brand-name">CALDERA</span></div>
  </section>

  <section class="piece envelope">
    <svg class="flap" viewBox="0 0 571 90" height="90" preserveAspectRatio="none">
      <defs>
        <linearGradient id="flapRed" x1="0" y1="0" x2="0" y2="1">
          <stop offset="0" stop-color="var(--red-deep)"/><stop offset="1" stop-color="var(--red-bright)"/>
        </linearGradient>
      </defs>
      <path d="M0 0 L571 0 L571 78 Q285 64 0 78 Z" fill="url(#flapRed)"/>
    </svg>
    <div class="brand on-red flap-brand"><span class="brand-dot"></span><span class="brand-name">CALDERA</span></div>
    <div class="brand return-brand"><span class="brand-dot"></span><span class="brand-name">CALDERA</span></div>
    <svg class="wave" viewBox="0 0 571 76" height="76" preserveAspectRatio="none">
      <path d="M0 14 Q285 40 571 8 L571 76 L0 76 Z" fill="var(--orange)"/>
      <path d="M0 20 Q285 46 571 16 L571 76 L0 76 Z" fill="url(#flapRed)"/>
    </svg>
    <p class="footer-text">PO BOX 7312 ASHMORE, CA 90512</p>
  </section>

</body>
</html>
```